Personnel recruitment Brauwalter GmbH

We would like to create an attractive flyer that focuses on one of our services in Saarland and Rhineland-Palatinate. The benefits for the customer should be presented.

```html
<!DOCTYPE html>
<html lang="de">
<head>
<meta charset="utf-8">
<title>Personalvermittlung – Brauwalter GmbH</title>
<link href="https://fonts.googleapis.com/css2?family=Montserrat:wght@400;600;700&display=swap" rel="stylesheet">
<style>
  :root{
    --dark:#2b2c30;
    --teal:#1f9f9f;
    --teal-text:#3aa8a6;
    --teal-light:#8fd0ce;
    --white:#ffffff;
    --ink:#2a2b30;
  }
  *{margin:0;padding:0;box-sizing:border-box}
  html,body{width:848px;height:1200px;overflow:hidden;background:var(--white)}
  .flyer{position:relative;width:848px;height:1200px;overflow:hidden;background:var(--dark);font-family:'Montserrat',sans-serif}
  .backdrop{position:absolute;left:0;top:0}
  .brand{position:absolute;left:63px;top:58px;display:flex;align-items:center;gap:10px}
  .brand-square{width:22px;height:22px;background:var(--teal);border:2px solid var(--white)}
  .brand-name{color:var(--white);font-weight:600;font-size:17px;letter-spacing:.5px}
  .title{position:absolute;left:61px;top:156px;font-size:51px;font-weight:700;color:var(--teal);letter-spacing:-.5px;line-height:1}
  .subtitle{position:absolute;left:63px;top:214px;font-size:16.5px;font-weight:700;color:var(--white);letter-spacing:.2px}
  .intro{position:absolute;left:63px;top:246px;width:780px;font-size:14.9px;line-height:21.5px;color:var(--teal-text);letter-spacing:.15px;white-space:nowrap}
  .section-title{position:absolute;left:63px;top:343px;font-size:27px;font-weight:700;color:var(--white);letter-spacing:.3px}
  .services{position:absolute;left:0;top:387px;list-style:none}
  .service{position:absolute;left:72px;height:43px;display:flex;align-items:center;gap:8px;color:var(--ink);font-size:15.6px;line-height:21.5px;letter-spacing:.2px;white-space:nowrap}
  .check{flex:none;width:28px;height:28px}
  .benefits-title{position:absolute;left:71px;top:703px;font-size:21.5px;line-height:23px;font-weight:700;color:var(--white);letter-spacing:.3px}
  .benefits{position:absolute;left:0;top:0;list-style:none}
  .benefit{position:absolute;display:flex;align-items:center;gap:8px;color:var(--teal-text);font-size:15.6px;line-height:21.5px;letter-spacing:.2px;white-space:nowrap}
  .contact{position:absolute;left:89px;top:1078px;color:var(--ink)}
  .contact-title{font-size:11.3px;font-weight:700;letter-spacing:.2px}
  .contact-list{list-style:none;margin:6px 0 0 18px}
  .contact-item{display:flex;align-items:center;gap:7px;height:19.5px;font-size:8.6px;font-weight:700;letter-spacing:.2px}
  .contact-icon{width:17px;height:17px;flex:none}
</style>
</head>
<body>
<div class="flyer">
  <svg class="backdrop" width="848" height="1200" viewBox="0 0 848 1200" aria-hidden="true">
    <defs>
      <linearGradient id="photoTone" x1="0" y1="0" x2="0.3" y2="1">
        <stop offset="0" stop-color="#4466c4"/>
        <stop offset="0.35" stop-color="#6f7fa8"/>
        <stop offset="0.6" stop-color="#8b9194"/>
        <stop offset="1" stop-color="#cfcac2"/>
      </linearGradient>
      <clipPath id="canvasClip"><rect width="848" height="1200"/></clipPath>
    </defs>
    <g clip-path="url(#canvasClip)">
      <!-- service bands -->
      <path d="M0 387 H762 Q778 387 786 404 Q820 412 848 430 V470 H0 Z" fill="var(--teal-light)"/>
      <rect x="0" y="450" width="600" height="52" fill="var(--teal-light)"/>
      <rect x="0" y="512" width="600" height="51" fill="var(--teal-light)"/>
      <rect x="0" y="574" width="600" height="51" fill="var(--teal-light)"/>
      <rect x="0" y="635" width="600" height="53" fill="var(--teal-light)"/>
      <path d="M0 438 H560 L540 450 H0 Z" fill="var(--dark)"/>
      <path d="M0 502 H485 L470 512 H0 Z" fill="var(--dark)"/>
      <path d="M0 563 H442 L432 574 H0 Z" fill="var(--dark)"/>
      <path d="M0 625 H420 L415 635 H0 Z" fill="var(--dark)"/>
      <rect x="600" y="470" width="248" height="220" fill="var(--teal-light)"/>
      <!-- photo ring -->
      <circle cx="711" cy="697" r="303" fill="var(--teal-light)"/>
      <!-- lower waves -->
      <path d="M0 880 C 300 990 560 1040 815 980 L815 987 C 560 1048 300 998 0 888 Z" fill="var(--teal-light)"/>
      <path d="M0 908 C 260 1000 560 1050 848 1000 V1120 H0 Z" fill="var(--teal-light)"/>
      <path d="M0 983 C 200 1000 400 1050 620 1055 C 720 1055 800 1040 848 1030 L848 1042 C 760 1066 650 1086 560 1086 C 350 1082 150 1042 0 1040 Z" fill="var(--dark)"/>
      <path d="M0 1040 C 150 1035 300 1080 560 1118 C 700 1126 800 1100 848 1082 V1200 H0 Z" fill="var(--white)"/>
    </g>
    <circle cx="711" cy="697" r="289" fill="url(#photoTone)" role="img" aria-label="Photo of the company building with a tall standing sign in front"/>
  </svg>

  <div class="brand">
    <span class="brand-square"></span>
    <span class="brand-name">BRAUWALTER GMBH</span>
  </div>

  <h1 class="title">PERSONALVERMITTLUNG</h1>
  <p class="subtitle">EFFIZIENTE LÖSUNGEN FÜR IHRE PERSONALSUCHE</p>
  <p class="intro">Passende Mitarbeiter zu finden, stellt heute eine große Herausforderung dar.<br>Profitieren Sie von unserem Netzwerk und unserer langjährigen Erfahrung im Recruiting.<br>Entlasten Sie Ihre Abteilungsleiter und fokussieren Sie sich auf Ihr Kerngeschäft, indem Sie<br>uns mit der Personalvermittlung beauftragen.</p>

  <h2 class="section-title">UNSERE DIENSTLEISTUNG</h2>

  <ul class="services">
    <li class="service" style="top:4px">
      <svg class="check" viewBox="0 0 28 28"><rect x="2" y="2" width="24" height="24" rx="4" fill="none" stroke="var(--ink)" stroke-width="2.6"/><path d="M8.5 14.5 L12.5 18 L19.5 10" fill="none" stroke="var(--ink)" stroke-width="2.6" stroke-linecap="round" stroke-linejoin="round"/></svg>
      <span>Erstellung des Anforderungsprofils mit einem<br>erfahrenen Recruiter</span>
    </li>
    <li class="service" style="top:68px">
      <svg class="check" viewBox="0 0 28 28"><rect x="2" y="2" width="24" height="24" rx="4" fill="none" stroke="var(--ink)" stroke-width="2.6"/><path d="M8.5 14.5 L12.5 18 L19.5 10" fill="none" stroke="var(--ink)" stroke-width="2.6" stroke-linecap="round" stroke-linejoin="round"/></svg>
      <span>Gestaltung und Veröffentlichung der<br>Stellenanzeige</span>
    </li>
    <li class="service" style="top:129px;left:71px">
      <svg class="check" viewBox="0 0 28 28"><rect x="2" y="2" width="24" height="24" rx="4" fill="none" stroke="var(--ink)" stroke-width="2.6"/><path d="M8.5 14.5 L12.5 18 L19.5 10" fill="none" stroke="var(--ink)" stroke-width="2.6" stroke-linecap="round" stroke-linejoin="round"/></svg>
      <span>Bewerberselektion für jede Qualifikation<br>und Hierarchiestufe</span>
    </li>
    <li class="service" style="top:191px">
      <svg class="check" viewBox="0 0 28 28"><rect x="2" y="2" width="24" height="24" rx="4" fill="none" stroke="var(--ink)" stroke-width="2.6"/><path d="M8.5 14.5 L12.5 18 L19.5 10" fill="none" stroke="var(--ink)" stroke-width="2.6" stroke-linecap="round" stroke-linejoin="round"/></svg>
      <span>Präsentation ausgewählter<br>Kandidaten oder aller bewerber</span>
    </li>
    <li class="service" style="top:253px">
      <svg class="check" viewBox="0 0 28 28"><rect x="2" y="2" width="24" height="24" rx="4" fill="none" stroke="var(--ink)" stroke-width="2.6"/><path d="M8.5 14.5 L12.5 18 L19.5 10" fill="none" stroke="var(--ink)" stroke-width="2.6" stroke-linecap="round" stroke-linejoin="round"/></svg>
      <span>Unterstützung beim Onboarding</span>
    </li>
  </ul>

  <h2 class="benefits-title">VORTEILE DER<br>PERSONALVERMITTLUNG</h2>

  <ul class="benefits">
    <li class="benefit" style="left:87px;top:763px">
      <svg class="check" viewBox="0 0 28 28"><rect x="2" y="2" width="24" height="24" rx="4" fill="none" stroke="var(--teal-light)" stroke-width="2.6"/><path d="M8.5 14.5 L12.5 18 L19.5 10" fill="none" stroke="var(--teal-light)" stroke-width="2.6" stroke-linecap="round" stroke-linejoin="round"/></svg>
      <span>Zeitersparnis und Entlastung für Ihr<br>Unternehmen</span>
    </li>
    <li class="benefit" style="left:89px;top:811px">
      <svg class="check" viewBox="0 0 28 28"><rect x="2" y="2" width="24" height="24" rx="4" fill="none" stroke="var(--teal-light)" stroke-width="2.6"/><path d="M8.5 14.5 L12.5 18 L19.5 10" fill="none" stroke="var(--teal-light)" stroke-width="2.6" stroke-linecap="round" stroke-linejoin="round"/></svg>
      <span>Jahrelange Erfahrung in der<br>Rekrutierung</span>
    </li>
    <li class="benefit" style="left:91px;top:859px">
      <svg class="check" viewBox="0 0 28 28"><rect x="2" y="2" width="24" height="24" rx="4" fill="none" stroke="var(--teal-light)" stroke-width="2.6"/><path d="M8.5 14.5 L12.5 18 L19.5 10" fill="none" stroke="var(--teal-light)" stroke-width="2.6" stroke-linecap="round" stroke-linejoin="round"/></svg>
      <span>Größeres Bewerbernetzwerk für<br>schnellere Ergebnisse</span>
    </li>
  </ul>

  <div class="contact">
    <p class="contact-title">KONTAKTIEREN SIE UNS NOCH HEUTE!</p>
    <ul class="contact-list">
      <li class="contact-item">
        <svg class="contact-icon" viewBox="0 0 18 18"><circle cx="9" cy="9" r="8.5" fill="var(--ink)"/><rect x="4.5" y="5.8" width="9" height="6.4" rx="0.8" fill="none" stroke="var(--white)" stroke-width="1"/><path d="M4.8 6.2 L9 9.6 L13.2 6.2" fill="none" stroke="var(--white)" stroke-width="1"/></svg>
        <span>INFO@BRAUWALTER.ORG</span>
      </li>
      <li class="contact-item">
        <svg class="contact-icon" viewBox="0 0 18 18"><circle cx="9" cy="9" r="8.5" fill="var(--ink)"/><circle cx="9" cy="9" r="5" fill="none" stroke="var(--white)" stroke-width="1"/><ellipse cx="9" cy="9" rx="2.2" ry="5" fill="none" stroke="var(--white)" stroke-width="1"/><path d="M4 9 H14" stroke="var(--white)" stroke-width="1"/></svg>
        <span>WWW.BRAUWALTER.ORG</span>
      </li>
      <li class="contact-item">
        <svg class="contact-icon" viewBox="0 0 18 18"><circle cx="9" cy="9" r="8.5" fill="var(--ink)"/><path d="M6 4.5 L7.6 4.3 L8.4 6.8 L7.3 7.7 Q8.1 9.6 10.2 10.7 L11.1 9.6 L13.6 10.4 L13.4 12 Q12.8 13.4 11.2 13.2 Q6.2 12 4.9 6.7 Q4.8 5 6 4.5 Z" fill="var(--white)"/></svg>
        <span>+49 6881 47310</span>
      </li>
    </ul>
  </div>
</div>
</body>
</html>
```